EXTENDED Store hours to serve your healthcare needs

I'M LOOKING FOR A NICE FLYER THAT SHOWS THE FOLLOWING INFORMATION:

Logo
address
tel phone and fax
email address

Extending our hours to meet the growing healthcare needs of our community. Fast delivery service!

Monday - Thursday 10am-midnight
Friday 10am-4pm
Saturday - Motzei Shabbos till midnight
Sunday 10am-7pm

Target Market(s)

Community

Industry/Entity Type

Pharmacy

Requirements
Must have
• Extended hours
• personal care
• expert advice
• superior service
Nice to have
• Looking for no people pictures
• Eye popping design
• Classic modern clean design
Should not have
• store description is services
• And should not say Fiirst to open and last to close

```html
<!DOCTYPE html>
<html lang="en">
<head>
<meta charset="utf-8">
<title>Halden Pharmacy – Extended Hours</title>
<link rel="stylesheet" href="https://fonts.googleapis.com/css2?family=Alfa+Slab+One&family=Roboto+Condensed:wght@300;400;700&display=swap">
<style>
  :root {
    --white: #ffffff;
    --brand-red: #c8242b;
    --bright-red: #e21f26;
    --sky-blue: #1ba3dc;
    --royal-blue: #2c4fa3;
    --navy: #1f3f8f;
    --silver: #c7c9cc;
    --ink: #111111;
    --slate: #5a5d61;
  }
  * { margin: 0; padding: 0; box-sizing: border-box; }
  html, body { width: 900px; height: 1200px; overflow: hidden; background: var(--white); }
  .flyer {
    position: relative; width: 900px; height: 1200px; overflow: hidden;
    font-family: "Roboto Condensed", Arial, sans-serif;
  }
  .shop-backdrop {
    position: absolute; inset: 0;
    background: radial-gradient(ellipse at 75% 35%, #e6ebee 0%, #f3f5f6 45%, var(--white) 75%);
  }
  .artwork { position: absolute; left: 0; top: 0; }
  .brand {
    position: absolute; left: 68px; top: 44px;
    display: flex; align-items: center; gap: 16px;
  }
  .brand-dot { width: 46px; height: 46px; border-radius: 50%; background: var(--royal-blue); }
  .brand-name {
    font-weight: 700; font-size: 60px; color: var(--brand-red); letter-spacing: 1px;
  }
  .pillar {
    position: absolute; border-radius: 50%;
    display: flex; flex-direction: column; align-items: center; justify-content: center;
    text-align: center; box-shadow: 0 0 0 6px var(--white);
  }
  .pillar-small {
    font-weight: 300; font-size: 42px; letter-spacing: 0.5px; line-height: 1;
  }
  .pillar-big {
    font-family: "Alfa Slab One", Georgia, serif; line-height: 1.1;
  }
  .pillar-care { left: 622px; top: 110px; width: 266px; height: 266px; background: var(--sky-blue); color: var(--white); padding-bottom: 10px; }
  .pillar-care .pillar-big { font-size: 62px; }
  .pillar-advice { left: 622px; top: 330px; width: 266px; height: 266px; background: var(--royal-blue); color: #dfe6f5; padding-bottom: 70px; }
  .pillar-advice .pillar-big { font-size: 46px; }
  .pillar-service { left: 625px; top: 500px; width: 260px; height: 260px; background: var(--silver); color: var(--ink); padding-bottom: 60px; }
  .pillar-service .pillar-big { font-size: 40px; }
  .new-hours {
    position: absolute; left: 620px; top: 710px; width: 270px;
    text-align: center; font-weight: 700; font-size: 32px;
    letter-spacing: 1px; color: var(--white);
  }
  .clock-label {
    position: absolute; left: 40px; top: 570px; width: 260px;
    text-align: center; font-family: "Alfa Slab One", Georgia, serif;
    color: var(--brand-red); line-height: 1; transform: rotate(7deg);
  }
  .clock-label span { display: block; }
  .clock-label .line-1 { font-size: 40px; }
  .clock-label .line-2 { font-size: 52px; }
  .schedule {
    position: absolute; right: 36px; top: 864px; text-align: right;
    color: var(--white); font-size: 42px; line-height: 44px;
  }
  .schedule-row { margin-bottom: 19px; }
  .schedule-day { font-weight: 400; }
  .schedule-time { font-weight: 700; }
  .badge { position: absolute; left: 12px; top: 862px; width: 296px; height: 296px; }
  .badge-text {
    position: absolute; left: 12px; top: 862px; width: 296px; height: 296px;
    display: flex; flex-direction: column; align-items: center; justify-content: center;
    text-align: center; color: var(--slate);
  }
  .badge-kicker { font-weight: 700; font-size: 22px; line-height: 1; }
  .badge-main { font-weight: 700; font-size: 32px; line-height: 1.05; }
  .badge-sub { font-size: 16px; margin-bottom: 18px; }
  .badge-fast { font-family: "Alfa Slab One", Georgia, serif; font-size: 60px; color: var(--ink); line-height: 1; }
  .badge-delivery { font-weight: 700; font-size: 22px; color: var(--ink); line-height: 1.1; }
  .badge-allday { font-family: "Alfa Slab One", Georgia, serif; font-size: 26px; color: var(--ink); line-height: 1.1; }
</style>
</head>
<body>
<main class="flyer">
  <div class="shop-backdrop" role="img" aria-label="Softly blurred pharmacy shelves in the background"></div>

  <svg class="artwork" width="900" height="1200" viewBox="0 0 900 1200">
    <g role="img" aria-label="Wall clock with hands at five minutes to twelve">
      <circle cx="175" cy="540" r="335" fill="var(--navy)"/>
      <circle cx="175" cy="545" r="318" fill="var(--sky-blue)"/>
      <circle cx="175" cy="545" r="290" fill="var(--white)"/>
    </g>
  </svg>

  <header class="brand">
    <span class="brand-dot"></span>
    <span class="brand-name">Halden Pharmacy</span>
  </header>

  <div class="pillar pillar-care">
    <span class="pillar-small">PERSONAL</span>
    <span class="pillar-big">CARE</span>
  </div>
  <div class="pillar pillar-advice">
    <span class="pillar-small">EXPERT</span>
    <span class="pillar-big">ADVICE</span>
  </div>
  <div class="pillar pillar-service">
    <span class="pillar-small">SUPERIOR</span>
    <span class="pillar-big">SERVICE</span>
  </div>

  <svg class="artwork" width="900" height="1200" viewBox="0 0 900 1200" aria-hidden="true">
    <path class="white-swoosh" d="M0,820 C230,875 470,800 630,748 C740,712 830,692 900,686 L900,706 C820,712 740,730 632,766 C470,818 230,898 0,842 Z" fill="#ffffff"/>
    <path class="red-band" d="M0,842 C230,898 470,818 632,766 C740,730 820,712 900,706 L900,1200 L0,1200 Z" fill="var(--brand-red)"/>
    <path class="new-hours-tab" d="M572,770 C650,715 770,694 900,692 L900,772 Z" fill="var(--bright-red)" stroke="#ffffff" stroke-width="4"/>
  </svg>

  <p class="new-hours">NEW HOURS</p>

  <h1 class="clock-label">
    <span class="line-1">EXTENDED</span>
    <span class="line-2">HOURS</span>
  </h1>

  <section class="schedule">
    <p class="schedule-row"><span class="schedule-day">MON - THU: </span><span class="schedule-time">10am till Midnight</span></p>
    <p class="schedule-row"><span class="schedule-day">FRIDAY: </span><span class="schedule-time">10am - 4pm</span></p>
    <p class="schedule-row"><span class="schedule-day">SATURDAY: </span><span class="schedule-time">Motzei Shabbos<br>till Midnight</span></p>
    <p class="schedule-row"><span class="schedule-day">SUNDAY: </span><span class="schedule-time">10am - 7pm</span></p>
  </section>

  <svg class="badge" viewBox="0 0 100 100" aria-hidden="true">
    <defs>
      <linearGradient id="badge-metal" x1="0" y1="0" x2="0" y2="1">
        <stop offset="0" stop-color="#f2f2f2"/>
        <stop offset="0.5" stop-color="#d9dadc"/>
        <stop offset="1" stop-color="#bfc1c4"/>
      </linearGradient>
    </defs>
    <polygon fill="url(#badge-metal)" stroke="#ffffff" stroke-width="0.8" points="100,50 93.5,56.9 97.6,65.5 89.2,70 90.5,79.4 81.1,81.1 79.4,90.5 70,89.2 65.5,97.6 56.9,93.5 50,100 43.1,93.5 34.5,97.6 30,89.2 20.6,90.5 18.9,81.1 9.5,79.4 10.8,70 2.4,65.5 6.5,56.9 0,50 6.5,43.1 2.4,34.5 10.8,30 9.5,20.6 18.9,18.9 20.6,9.5 30,10.8 34.5,2.4 43.1,6.5 50,0 56.9,6.5 65.5,2.4 70,10.8 79.4,9.5 81.1,18.9 90.5,20.6 89.2,30 97.6,34.5 93.5,43.1"/>
  </svg>
  <div class="badge-text">
    <span class="badge-kicker">EXTENDING</span>
    <span class="badge-main">OUR HOURS</span>
    <span class="badge-sub">to meet your needs</span>
    <span class="badge-fast">FAST</span>
    <span class="badge-delivery">DELIVERY SERVICE</span>
    <span class="badge-allday">ALL DAY</span>
  </div>
</main>
</body>
</html>
```